Commercial and Multifamily informational website

We need a website for our commercial real estate management company. We will manage offices, retail, apartments and others. Here is the brief verbiage: Providing quality commercial and multifamily portfolio management to Landlords, REITs, and financial institutions. 

Industry/Entity Type

Real Estate

Number of Pages Required

2 page

Font styles to use
Sans Serif
Other font styles liked:
• Muli, Garamond

Colors
0555a3
5c5c5c
3176b5
85acd3
474747

Requirements
Must have
• Home page and contact page

```html
<!DOCTYPE html>
<html lang="en">
<head>
<meta charset="utf-8">
<title>Halvern Real Estate Management</title>
<link href="https://fonts.googleapis.com/css2?family=Lato:wght@400;700;900&display=swap" rel="stylesheet">
<style>
:root{
  --brand:#0555a3;
  --brand-deep:#0a3b8a;
  --ink:#474747;
  --ink-soft:#5c5c5c;
  --sky:#85acd3;
  --mid:#3176b5;
  --grey-bg:#eeeeee;
  --footer:#262626;
  --white:#ffffff;
}
*{margin:0;padding:0;box-sizing:border-box}
html,body{width:742px;height:1200px;overflow:hidden}
body{font-family:'Lato',sans-serif;color:var(--ink);background:var(--white);position:relative}
.abs{position:absolute}

/* header */
.site-header{position:absolute;left:0;top:0;width:742px;height:56px;background:var(--white)}
.brand{position:absolute;left:50px;top:17px;display:flex;align-items:center;gap:6px}
.brand-mark{width:12px;height:12px;background:var(--brand)}
.brand-name{font-size:12px;font-weight:700;color:var(--brand);line-height:1.1;width:120px}
.main-nav{position:absolute;top:22px;left:322px;display:flex;gap:29px;font-size:11px;font-weight:700;color:var(--ink-soft)}
.main-nav .active{color:var(--brand)}
.call{position:absolute;left:595px;top:14px;display:flex;align-items:center;gap:8px}
.call-divider{width:1px;height:26px;background:var(--ink-soft)}
.call-text{font-size:9px;font-weight:700;color:var(--brand);line-height:1.4}
.call-text b{color:#111;display:block}

/* hero */
.hero{position:absolute;left:0;top:56px;width:742px;height:280px;
  background:linear-gradient(180deg,#5d6f86 0%,#4a5466 45%,#3a3530 75%,#2d2a28 100%)}
.hero-title{position:absolute;left:0;top:96px;width:742px;text-align:center;color:var(--white);
  font-size:14.4px;font-weight:700;line-height:21px;letter-spacing:.3px}
.hero-btn{position:absolute;left:318px;top:150px;width:105px;height:29px;border:1.5px solid var(--white);
  color:var(--white);font-size:10px;font-weight:700;text-align:center;line-height:26px}
.hero-arrow{position:absolute;top:128px}

/* welcome */
.welcome-title{position:absolute;left:0;top:358px;width:742px;text-align:center;font-size:20px;font-weight:700;color:var(--ink)}
.welcome-title span{color:var(--brand)}
.rule{position:absolute;height:1px;background:var(--ink-soft)}
.lead{position:absolute;left:0;top:411px;width:742px;text-align:center;font-size:11px;font-weight:700;color:#222}
.body-copy{position:absolute;left:56px;top:435px;width:630px;text-align:center;font-size:8.4px;line-height:14px;color:var(--ink)}
.outline-btn{position:absolute;left:329px;top:512px;width:83px;height:28px;border:1.5px solid var(--brand);
  font-size:10px;font-weight:700;color:#222;text-align:center;line-height:25px}

/* services */
.services{position:absolute;left:0;top:570px;width:742px;height:410px;background:var(--grey-bg)}
.services-title{position:absolute;left:0;top:28px;width:742px;text-align:center;font-size:22px;font-weight:700;color:var(--ink)}
.services-title span{color:var(--brand)}
.tile{position:absolute;overflow:hidden}
.tile-label{position:absolute;left:0;bottom:0;width:100%;height:32px;background:rgba(40,40,40,.72);
  color:var(--white);font-size:11px;font-weight:700;text-align:center;line-height:32px;letter-spacing:.3px}

/* footer */
.site-footer{position:absolute;left:0;top:980px;width:742px;height:190px;background:var(--footer);color:var(--white)}
.foot-h{position:absolute;top:26px;font-size:11.5px;font-weight:700}
.foot-rule{position:absolute;top:46px;height:1px;background:#555}
.foot-links{position:absolute;left:49px;top:55px;list-style:none;font-size:8px;line-height:22.6px}
.foot-contact{position:absolute;left:174px;top:56px;font-size:8px;line-height:13px}
.foot-row{position:absolute;left:174px;display:flex;align-items:center;gap:8px;font-size:8px}
.field{position:absolute;left:368px;width:165px;border:1px solid #555;background:#1c1c1c;font-size:8px;font-weight:700;padding:6px 8px}
.submit{position:absolute;left:368px;top:141px;width:65px;height:22px;background:var(--brand-deep);font-size:8px;font-weight:700;text-align:center;line-height:22px}
.foot-brand{position:absolute;left:563px;top:64px;width:130px;font-size:11px;font-weight:700;color:#cfcfcf;line-height:1.2}
.socials{position:absolute;left:601px;top:117px;display:flex;gap:4px}
.socials span{width:18px;height:18px;border-radius:50%;background:var(--mid);border:1.5px solid var(--white)}
.copyright{position:absolute;left:0;top:1170px;width:742px;height:30px;background:var(--brand-deep);color:var(--white);
  font-size:8px;text-align:center;line-height:30px}
</style>
</head>
<body>

<header class="site-header">
  <div class="brand"><span class="brand-mark"></span><span class="brand-name">Halvern Real Estate Management</span></div>
  <nav class="main-nav"><span class="active">HOME</span><span>ABOUT</span><span>SERVICES</span><span>CONTACT</span></nav>
  <div class="call">
    <svg width="22" height="22" viewBox="0 0 24 24" aria-hidden="true"><path d="M6.6 10.8a15 15 0 006.6 6.6l2.2-2.2c.3-.3.7-.4 1-.2 1.1.4 2.3.6 3.6.6.6 0 1 .4 1 1V20c0 .6-.4 1-1 1A17 17 0 013 4c0-.6.4-1 1-1h3.5c.6 0 1 .4 1 1 0 1.3.2 2.5.6 3.6.1.3 0 .7-.2 1z" fill="var(--brand)"/><path d="M15 3a6 6 0 016 6M15 6.5a2.5 2.5 0 012.5 2.5" stroke="var(--brand)" stroke-width="1.6" fill="none"/></svg>
    <span class="call-divider"></span>
    <div class="call-text">CALL US<b>(555)-210-4836</b></div>
  </div>
</header>

<section class="hero" role="img" aria-label="City skyline of office towers under a cloudy sky">
  <svg class="hero-arrow" style="left:33px" width="14" height="24" viewBox="0 0 14 24" aria-hidden="true"><path d="M12 1L2 12l10 11" stroke="#fff" stroke-width="2" fill="none"/></svg>
  <svg class="hero-arrow" style="left:695px" width="14" height="24" viewBox="0 0 14 24" aria-hidden="true"><path d="M2 1l10 11L2 23" stroke="#fff" stroke-width="2" fill="none"/></svg>
  <h1 class="hero-title">PROVIDING QUALITY COMMERCIAL &amp; MULTIFAMILY PORTFOLIO<br>MANAGEMENT TO LANDLORDS, REITS, &amp; FINANCIAL INSTITUTIONS</h1>
  <div class="hero-btn">CONTACT NOW!</div>
</section>

<h2 class="welcome-title">WELCOME TO <span>HALVERN</span></h2>
<div class="rule" style="left:231px;top:391px;width:279px"></div>
<div class="rule" style="left:264px;top:388px;width:230px;background:var(--brand)"></div>
<p class="lead">Lorem ipsum dolor sit amet, consectetuer adipiscing elit, sed diam nonummy nibh euismod tincidun.</p>
<p class="body-copy">Lorem ipsum dolor sit amet, consectetuer adipiscing elit, sed diam nonummy nibh euismod tincidunt ut laoreet dolore magna aliquam erat volutpat. Ut wisi enim ad minim veniam, quis nostrud exerci tation ullamcorper suscipit lobortis nisl ut aliquip ex ea commodo consequat. Duis autem vel eum iriure dolor in hendrerit in vulputate velit esse molestie consequat, vel illum dolore eu feugiat nulla facilisis at vero eros et accumsan et iusto odio dignissim qui blandit praesent luptatum zzril delenit augue duis dolore te feugait nulla facilisi suscipit lobortis nisl ut aliquip ex ea commodo consequat.</p>
<div class="outline-btn">READ MORE</div>

<section class="services">
  <h2 class="services-title">OUR <span>SERVICES</span></h2>
  <div class="rule" style="left:289px;top:60px;width:164px"></div>
  <div class="rule" style="left:298px;top:57px;width:146px;background:var(--brand)"></div>

  <div class="tile" style="left:50px;top:88px;width:309px;height:285px;background:linear-gradient(180deg,#3d86c9 0%,#9cc3e3 45%,#c9cfcf 75%,#6f7a5e 100%)" role="img" aria-label="White high-rise apartment tower by the beach">
    <div class="tile-label">APARTMENTS</div></div>
  <div class="tile" style="left:381px;top:88px;width:144px;height:135px;background:linear-gradient(180deg,#e4e4e4 0%,#bdbdbd 55%,#4a4a4a 100%)" role="img" aria-label="Modern office meeting room with chairs">
    <div class="tile-label">MANAGE OFFICES</div></div>
  <div class="tile" style="left:547px;top:88px;width:145px;height:135px;background:linear-gradient(135deg,#5a5a5a 0%,#8a3a3a 45%,#3f5f6b 100%)" role="img" aria-label="Shopping mall storefronts">
    <div class="tile-label">RETAIL</div></div>
  <div class="tile" style="left:381px;top:238px;width:311px;height:135px;background:linear-gradient(180deg,#6e85a8 0%,#8c8a80 50%,#3c3226 100%)" role="img" aria-label="Two-storey house lit at dusk">
    <div class="tile-label">OTHER PROPERTIES</div></div>
</section>

<footer class="site-footer">
  <h3 class="foot-h" style="left:49px">QUICK LINKS</h3>
  <h3 class="foot-h" style="left:172px">CONTACT DETAILS</h3>
  <h3 class="foot-h" style="left:367px">QUICK INQUIRY</h3>
  <div class="foot-rule" style="left:49px;width:83px"></div>
  <div class="foot-rule" style="left:172px;width:154px"></div>
  <div class="foot-rule" style="left:367px;width:166px"></div>
  <div class="abs" style="left:150px;top:56px;width:1px;height:120px;background:#3a3a3a"></div>
  <div class="abs" style="left:340px;top:56px;width:1px;height:120px;background:#3a3a3a"></div>

  <ul class="foot-links"><li>• Home</li><li>• About</li><li>• Services</li><li>• Contact</li></ul>
  <div class="foot-contact"><b>Halvern Real Estate Management</b><br>48 Harbor View Plaza, Suite 210,<br>Brookfield, NY - 10452</div>
  <div class="foot-row" style="top:105px"><svg width="9" height="9" viewBox="0 0 24 24" aria-hidden="true"><path d="M6.6 10.8a15 15 0 006.6 6.6l2.2-2.2c.3-.3.7-.4 1-.2 1.1.4 2.3.6 3.6.6.6 0 1 .4 1 1V20c0 .6-.4 1-1 1A17 17 0 013 4c0-.6.4-1 1-1h3.5c.6 0 1 .4 1 1 0 1.3.2 2.5.6 3.6.1.3 0 .7-.2 1z" fill="#fff"/></svg>555-210-4836</div>
  <div class="foot-row" style="top:128px"><svg width="9" height="9" viewBox="0 0 24 24" aria-hidden="true"><rect x="6" y="2" width="12" height="6" fill="#fff"/><rect x="2" y="9" width="20" height="9" fill="#fff"/><rect x="6" y="15" width="12" height="7" fill="#fff" stroke="#262626"/></svg>555-210-4837</div>
  <div class="foot-row" style="top:152px"><svg width="9" height="7" viewBox="0 0 24 18" aria-hidden="true"><rect width="24" height="18" fill="#fff"/><path d="M0 0l12 9 12-9" stroke="#262626" stroke-width="2" fill="none"/></svg>info@halvernrem.com</div>

  <div class="field" style="top:57px;height:20px;padding-top:5px">Name</div>
  <div class="field" style="top:83px;height:20px;padding-top:5px">Email</div>
  <div class="field" style="top:110px;height:27px;padding-top:5px">Message</div>
  <div class="submit">SUBMIT</div>

  <div class="foot-brand">Halvern Real Estate Management</div>
  <div class="socials" aria-label="Social links"><span></span><span></span><span></span></div>
</footer>
<div class="copyright">Copyright © 2017 Halvern Real Estate Management. All Right Reserved</div>

</body>
</html>
```